PostCard for Managed IT Services

We need a postcard design for a postcard that we intend to send out early in our marketing efforts to medical practices. The postcard should communicate our core services for small businesses including 1.) Managed IT Services, 2.) Security Services, 3.) Cloud Services, and 4.) IT Project and Integration work. company information is available at www.fernwaylab.com. I attached a two logos.WHILE WE WANT TO USE THE LOGO AND COLORS FROM OUR SITE, I HOPE THE DESIGN IS BOLD AND GRABS ATTENTION. I HOPE IT IS NOT THE 'SAME OLD' INFORMATION TECHNOLOGY LOOK. BE CREATIVE AND GET THE READER TO LOOK TWICE.

Target Market(s)

Businesses, medical practices

Font styles to use
Serif
Sans Serif

Requirements
Must have
• We need to include somewhere that are technicians are trained in on HIPAA and PCI (see site for info on the two)

```html
<!DOCTYPE html>
<html lang="en">
<head>
<meta charset="utf-8">
<title>Fernway Lab Postcard</title>
<link href="https://fonts.googleapis.com/css2?family=Barlow+Condensed:wght@400;500;600&display=swap" rel="stylesheet">
<style>
  :root {
    --backdrop: #e6e7ea;
    --paper: #ffffff;
    --navy: #2a2a72;
    --navy-deep: #1f1f5e;
    --violet: #4b3f86;
    --accent: #5a78c8;
    --ink: #1c1c1c;
    --white: #ffffff;
  }
  * { box-sizing: border-box; margin: 0; padding: 0; }
  html, body { width: 1200px; height: 480px; overflow: hidden; }
  body {
    background: var(--backdrop);
    font-family: "Barlow Condensed", "Arial Narrow", sans-serif;
    position: relative;
  }
  .card { position: absolute; top: 62px; height: 356px; background: var(--paper); overflow: hidden; }
  .card--front { left: 58px; width: 534px; }
  .card--back { left: 608px; width: 510px; }

  .brand-panel { position: absolute; top: 0; left: 0; width: 198px; height: 100%; }
  .photo-panel {
    position: absolute; top: 0; height: 100%;
    background: linear-gradient(160deg, var(--violet) 0%, var(--navy) 35%, var(--navy-deep) 100%);
    border-left: 4px solid var(--accent);
  }
  .card--front .photo-panel { left: 198px; right: 0; }
  .card--back .photo-panel { left: 0; width: 256px; border-left: none; border-right: 4px solid var(--accent); }

  .wordmark {
    position: absolute; left: 0; width: 100%; text-align: center;
    font-weight: 600; font-size: 22px; letter-spacing: 6px;
  }
  .tagline {
    position: absolute; left: 0; width: 100%; text-align: center;
    font-size: 8px; font-weight: 500; letter-spacing: 2.4px; line-height: 11px;
  }
  .brand-panel .wordmark, .brand-panel .tagline { color: var(--accent); }
  .photo-panel .wordmark, .photo-panel .tagline { color: var(--white); }

  .contact-item { position: absolute; display: flex; align-items: center; gap: 10px; }
  .contact-icon {
    width: 30px; height: 30px; border-radius: 50%; flex: none;
    display: flex; align-items: center; justify-content: center;
  }
  .contact-text { font-size: 13.5px; line-height: 15px; }
  .brand-panel .contact-icon { background: var(--accent); }
  .brand-panel .contact-text { color: var(--accent); }
  .photo-panel .contact-icon { background: var(--white); }
  .photo-panel .contact-text { color: var(--white); }

  .headline {
    position: absolute; top: 40px; left: 0; width: 100%; text-align: center;
    color: var(--white); font-weight: 500; font-size: 33px; line-height: 36px;
  }
  .subhead {
    position: absolute; top: 81px; left: 0; width: 100%; text-align: center;
    color: var(--white); font-size: 16px;
  }
  .service { position: absolute; width: 110px; text-align: center; }
  .service-badge {
    width: 74px; height: 74px; border-radius: 50%; background: var(--white);
    margin: 0 auto; display: flex; align-items: center; justify-content: center;
  }
  .service-label {
    color: var(--white); font-weight: 500; font-size: 16px; line-height: 15px;
    margin-top: 8px; text-transform: uppercase; white-space: nowrap;
  }

  .compliance-note {
    position: absolute; left: 276px; top: 40px; width: 140px;
    color: var(--accent); font-size: 14px; line-height: 17px; font-weight: 500;
  }

  .stamp-box { position: absolute; left: 434px; top: 34px; width: 68px; height: 67px; border: 1.5px solid var(--ink); }
  .address-line { position: absolute; left: 287px; width: 214px; height: 0; border-top: 1.5px solid var(--ink); }
</style>
</head>
<body>

<section class="card card--front">
  <div class="brand-panel">
    <div class="wordmark" style="top:72px;">Fernway Lab</div>
    <div class="tagline" style="top:137px;">Managed Services<br>Partner with the best!</div>

    <div class="contact-item" style="left:18px; top:185px;">
      <span class="contact-icon"><svg width="16" height="12" viewBox="0 0 16 12"><rect x="0.5" y="0.5" width="15" height="11" fill="#fff"/><path d="M0.5 0.5 L8 7 L15.5 0.5" fill="none" stroke="#5a78c8" stroke-width="1.2"/></svg></span>
      <span class="contact-text">Email:<br>info@fernwaylab.com</span>
    </div>
    <div class="contact-item" style="left:18px; top:231px;">
      <span class="contact-icon"><svg width="16" height="16" viewBox="0 0 24 24"><path fill="#fff" d="M6.6 10.8a15 15 0 0 0 6.6 6.6l2.2-2.2a1 1 0 0 1 1-.25 11.4 11.4 0 0 0 3.6.57 1 1 0 0 1 1 1V20a1 1 0 0 1-1 1A17 17 0 0 1 3 4a1 1 0 0 1 1-1h3.5a1 1 0 0 1 1 1c0 1.25.2 2.45.57 3.57a1 1 0 0 1-.25 1z"/></svg></span>
      <span class="contact-text">Phone:<br>(555) 014-2290</span>
    </div>
    <div class="contact-item" style="left:18px; top:277px;">
      <span class="contact-icon"><svg width="16" height="16" viewBox="0 0 24 24"><path fill="#fff" d="M12 2a7 7 0 0 0-7 7c0 5 7 13 7 13s7-8 7-13a7 7 0 0 0-7-7zm0 9.5A2.5 2.5 0 1 1 12 6.5a2.5 2.5 0 0 1 0 5z"/></svg></span>
      <span class="contact-text">Address:<br>118 Alder Row, Suite 4<br>Brookfield, ND 58000</span>
    </div>
  </div>

  <div class="photo-panel" role="img" aria-label="Close-up photo of a computer keyboard in deep blue light">
    <h1 class="headline">Fernway Managed Services</h1>
    <p class="subhead">Partner with the best for all your IT needs!</p>

    <div class="service" style="left:20px; top:121px;">
      <div class="service-badge"><svg width="44" height="44" viewBox="0 0 44 44"><path d="M12 8c-3 2-4 6-2 11 3 7 8 12 15 15 5 2 9 1 11-2l-5-5-4 3c-4-2-7-5-9-9l3-4z" fill="none" stroke="#5a78c8" stroke-width="2.4" stroke-linejoin="round"/><path d="M22 6a16 16 0 0 1 16 16" fill="none" stroke="#5a78c8" stroke-width="2"/><text x="30" y="20" font-family="Barlow Condensed, sans-serif" font-size="12" font-weight="600" fill="#5a78c8" text-anchor="middle">24</text></svg></div>
      <div class="service-label">Managed IT<br>Services</div>
    </div>
    <div class="service" style="left:111px; top:121px;">
      <div class="service-badge"><svg width="36" height="40" viewBox="0 0 36 40"><path d="M10 18v-6a8 8 0 0 1 16 0v6" fill="none" stroke="#5a78c8" stroke-width="3"/><rect x="5" y="18" width="26" height="19" rx="2" fill="none" stroke="#5a78c8" stroke-width="3"/><circle cx="18" cy="26" r="2.5" fill="#5a78c8"/><rect x="17" y="27" width="2" height="5" fill="#5a78c8"/></svg></div>
      <div class="service-label">Security<br>Services</div>
    </div>
    <div class="service" style="left:201px; top:121px;">
      <div class="service-badge"><svg width="44" height="36" viewBox="0 0 44 36"><path d="M12 30a8 8 0 0 1-1-16 11 11 0 0 1 21-2 9 9 0 0 1 1 18" fill="none" stroke="#5a78c8" stroke-width="2.4"/><path d="M18 20v-3a4 4 0 0 1 8 0v3" fill="none" stroke="#5a78c8" stroke-width="2"/><rect x="16" y="20" width="12" height="10" rx="1" fill="none" stroke="#5a78c8" stroke-width="2"/><circle cx="22" cy="25" r="1.5" fill="#5a78c8"/></svg></div>
      <div class="service-label">Cloud<br>Services</div>
    </div>
    <div class="service" style="left:59px; top:236px;">
      <div class="service-badge"><svg width="44" height="44" viewBox="0 0 44 44"><path d="M16 30c0-4-5-6-5-13a10 10 0 0 1 17-7" fill="none" stroke="#5a78c8" stroke-width="2.4"/><rect x="15" y="31" width="10" height="3" fill="#5a78c8"/><rect x="16" y="36" width="8" height="3" fill="#5a78c8"/><circle cx="30" cy="20" r="6" fill="none" stroke="#5a78c8" stroke-width="2.4"/><circle cx="30" cy="20" r="2" fill="#5a78c8"/><path d="M30 11v3M30 26v3M21 20h3M36 20h3M24 14l2 2M34 24l2 2M36 14l-2 2M24 26l2-2" stroke="#5a78c8" stroke-width="2"/></svg></div>
      <div class="service-label">IT Project</div>
    </div>
    <div class="service" style="left:149px; top:236px;">
      <div class="service-badge"><svg width="40" height="44" viewBox="0 0 40 44"><rect x="10" y="6" width="20" height="32" rx="2" fill="none" stroke="#5a78c8" stroke-width="2.4"/><circle cx="15" cy="11" r="1.5" fill="#5a78c8"/><path d="M3 13h7M3 20h7M3 27h7M3 34h7M30 13h7M30 20h7M30 27h7M30 34h7" stroke="#5a78c8" stroke-width="2"/></svg></div>
      <div class="service-label">Integration Work</div>
    </div>
  </div>
</section>

<section class="card card--back">
  <div class="photo-panel" role="img" aria-label="Close-up photo of a computer keyboard in deep blue light">
    <div class="wordmark" style="top:73px;">Fernway Lab</div>
    <div class="tagline" style="top:139px;">Managed Services<br>Partner with the best!</div>

    <div class="contact-item" style="left:27px; top:178px;">
      <span class="contact-icon"><svg width="16" height="12" viewBox="0 0 16 12"><rect x="0.5" y="0.5" width="15" height="11" fill="#2a2a72"/><path d="M0.5 0.5 L8 7 L15.5 0.5" fill="none" stroke="#fff" stroke-width="1.2"/></svg></span>
      <span class="contact-text">Email:<br>info@fernwaylab.com</span>
    </div>
    <div class="contact-item" style="left:27px; top:225px;">
      <span class="contact-icon"><svg width="16" height="16" viewBox="0 0 24 24"><path fill="#2a2a72" d="M6.6 10.8a15 15 0 0 0 6.6 6.6l2.2-2.2a1 1 0 0 1 1-.25 11.4 11.4 0 0 0 3.6.57 1 1 0 0 1 1 1V20a1 1 0 0 1-1 1A17 17 0 0 1 3 4a1 1 0 0 1 1-1h3.5a1 1 0 0 1 1 1c0 1.25.2 2.45.57 3.57a1 1 0 0 1-.25 1z"/></svg></span>
      <span class="contact-text">Phone:<br>(555) 014-2290</span>
    </div>
    <div class="contact-item" style="left:27px; top:275px;">
      <span class="contact-icon"><svg width="16" height="16" viewBox="0 0 24 24"><path fill="#2a2a72" d="M12 2a7 7 0 0 0-7 7c0 5 7 13 7 13s7-8 7-13a7 7 0 0 0-7-7zm0 9.5A2.5 2.5 0 1 1 12 6.5a2.5 2.5 0 0 1 0 5z"/></svg></span>
      <span class="contact-text">Address:<br>118 Alder Row<br>Suite 4 Brookfield, ND 58000</span>
    </div>
  </div>

  <p class="compliance-note">Our technicians are trained in HIPAA and PCI compliance.</p>

  <div class="stamp-box"></div>
  <div class="address-line" style="top:224px;"></div>
  <div class="address-line" style="top:266px;"></div>
  <div class="address-line" style="top:310px;"></div>
</section>

</body>
</html>
```